Flyer-Design für Handelsvertreung
Vielen Dank an Frau Wolmer für die gute Zusammenarbeit und die tollen Designs! mebuso4
Zielgruppe
Über Raumfunke GmbH:
Raumfunke ist eine junge Handelsvertretung in Hamburg.
Durch das breite Produktsortiment unserer Hersteller gewährleisten wir Ihnen eine optimale Auswahl und Betreuung von der Planungsphase bis zur Installation.
Auf Basis wirtschaftlicher, gestalterischer und technischer Bewertungskriterien beraten wir Sie bei der Auswahl ihrer Beleuchtungsanlagen.
Wir unterstützen Sie durch den Einsatz der richtigen Lichttechnik und tageslichtabhängigen Steuerungen dabei, Ihre Betriebskosten spürbar zu senken.
Um für Sie die bestmöglichen Beleuchtungskonzepte realisieren zu können, ist für uns entsprechendes Know-how in Bezug auf gesetzliche Bestimmungen unerlässlich.
www.raumfunke.de
Die Zielgruppe:
Die Zielgruppe der Raumfunke GmbH sind (Innen)Architekten, Designer und Planungsbüros.
Aufgabenstellung
Wir möchten einen modernen, einfach gestalteten Flyer,
welchen wir im Kundengespräch übergeben können.
Der Flyer soll unsere Produktbilder und unsere Dienstleistungen wiederspiegeln.

```html
<!DOCTYPE html>
<html lang="de">
<head>
<meta charset="utf-8">
<title>Raumfunke – Broschüre</title>
<link rel="stylesheet" href="https://fonts.googleapis.com/css2?family=Montserrat:wght@400;600;700&display=swap">
<style>
:root{
  --yellow:#f5e44f;
  --yellow-soft:#f7ea6e;
  --grey:#6b6b6b;
  --grey-dark:#555;
  --ink:#2c2c2c;
  --paper:#ffffff;
  --stage:#e8e8e8;
}
*{box-sizing:border-box;margin:0;padding:0}
html,body{width:1176px;height:1200px;overflow:hidden}
body{background:var(--stage);font-family:"Montserrat",sans-serif;color:var(--ink);position:relative}
.page{position:absolute;width:370px;height:523px;background:var(--paper);overflow:hidden;box-shadow:0 2px 8px rgba(0,0,0,.15)}
.page svg.shapes{position:absolute;inset:0;width:100%;height:100%}
.photo{position:absolute}
.photo.office{background:linear-gradient(160deg,#f4f4f4,#c9ccd1 60%,#8d9096)}
.photo.plan{background:linear-gradient(135deg,#f3f3f1 0%,#dfe0dc 55%,#3b3f48 100%)}
.photo.meeting-green{background:linear-gradient(180deg,#eef1f3,#c8cbc6 55%,#9a8a6a)}
.photo.meeting-warm{background:linear-gradient(180deg,#dfe6ee,#b8b3a2 50%,#4a4540)}
.photo.lamps{background:linear-gradient(135deg,#6a8a3a,#2d2d2d 55%,#e9e9e9)}
.photo.dark{background:linear-gradient(160deg,#d9dadc,#6d7075 60%,#3a3c40)}
.photo.lobby{background:linear-gradient(160deg,#f1f1f3,#b7a9c4 55%,#8d8f94)}
.photo.wood{background:linear-gradient(120deg,#f2f2f2,#c79b6e 55%,#e8e8e8)}
.photo.car{background:linear-gradient(160deg,#eef2f6,#b9c1cb 60%,#7f8790)}
.abs{position:absolute}

/* cover */
.cover{left:200px;top:40px}
.brand{position:absolute;left:40px;top:34px;display:flex;align-items:center;gap:7px;font-weight:600;font-size:21px;letter-spacing:.5px;color:var(--ink)}
.brand .dot{width:14px;height:14px;border-radius:50%;background:var(--yellow)}
.url-band{position:absolute;left:0;top:491px;width:350px;height:20px;background:var(--yellow);font-weight:700;font-size:11px;text-align:center;line-height:20px}

/* back */
.back{left:606px;top:40px}
.contact{position:absolute;left:0;right:0;top:350px;text-align:center;font-size:9px;line-height:1.4}
.contact p+p{margin-top:10px}
.back .url{position:absolute;left:0;right:0;top:478px;text-align:center;font-weight:700;font-size:11px}

/* spread */
.spread-left{left:218px;top:623px;box-shadow:none}
.spread-right{left:588px;top:623px;box-shadow:none}
.spread-frame{position:absolute;left:218px;top:623px;width:740px;height:523px;box-shadow:0 2px 8px rgba(0,0,0,.15)}
.tab{position:absolute;color:#fff;font-weight:700;font-size:9px;letter-spacing:.5px;padding:4px 20px 4px 10px;background:var(--grey-dark);clip-path:polygon(0 0,100% 0,88% 100%,0 100%)}
.copy{position:absolute;font-size:7px;line-height:1.38}
.copy p+p{margin-top:5px}
.about{left:22px;top:90px;width:326px}
.service-a{left:14px;top:222px;width:160px}
.service-b{left:188px;top:222px;width:160px}
.range{position:absolute;left:196px;top:78px;width:166px;height:108px;background:var(--grey);color:#fff;padding:9px 10px;clip-path:polygon(0 0,100% 0,100% 80%,90% 100%,0 100%)}
.range h3{color:var(--yellow);font-size:7.5px;line-height:1.2;font-weight:700;margin-bottom:4px}
.range ul{list-style:none;font-size:6.6px;line-height:1.42}
.range li::before{content:"";display:inline-block;width:0;height:0;border-left:4px solid var(--yellow);border-top:2.5px solid transparent;border-bottom:2.5px solid transparent;margin-right:4px}
</style>
</head>
<body>

<!-- Titelseite -->
<section class="page cover">
  <div class="photo plan" style="left:0;top:0;width:370px;height:300px" role="img" aria-label="Foto: Hände mit Stift über einem Lichtplanungs-Grundriss mit Farbmustern"></div>
  <svg class="shapes" viewBox="0 0 370 523" aria-hidden="true">
    <polygon points="0,0 290,0 140,125 0,55" fill="#fff"/>
    <polygon points="0,240 0,300 150,300" fill="#6b6b6b"/>
    <polygon points="370,255 370,300 300,300" fill="#f5e44f"/>
    <polygon points="0,300 370,300 370,318 0,318" fill="#fff"/>
    <polygon points="318,282 370,258 370,312" fill="#f5e44f"/>
    <polygon points="350,491 370,481 370,511 350,511" fill="#6b6b6b"/>
  </svg>
  <div class="brand"><span class="dot"></span>RAUMFUNKE</div>
  <div class="photo meeting-green" style="left:12px;top:330px;width:172px;height:140px" role="img" aria-label="Foto: heller Besprechungsraum mit runden Deckenleuchten und grünen Stühlen"></div>
  <div class="photo meeting-warm" style="left:192px;top:330px;width:166px;height:140px" role="img" aria-label="Foto: großer Konferenzraum mit gelben Pendelleuchten"></div>
  <svg class="shapes" viewBox="0 0 370 523" aria-hidden="true">
    <polygon points="184,448 184,470 160,470" fill="#f5e44f"/>
    <polygon points="358,446 358,470 334,470" fill="#f5e44f"/>
  </svg>
  <div class="url-band">www.raumfunke.de</div>
</section>

<!-- Rückseite -->
<section class="page back">
  <div class="photo office" style="left:0;top:0;width:370px;height:320px" role="img" aria-label="Foto: Besprechungsraum mit Pendelleuchte über dem Tisch"></div>
  <div class="photo dark" style="left:220px;top:0;width:150px;height:330px;clip-path:polygon(30% 0,100% 0,100% 100%,0 0)" role="img" aria-label="Foto: Beratungsgespräch an einem Tisch"></div>
  <svg class="shapes" viewBox="0 0 370 523" aria-hidden="true">
    <polygon points="212,0 226,0 370,300 370,328" fill="#fff"/>
    <polygon points="0,290 250,290 370,345 370,523 0,523" fill="#f7ea6e"/>
    <polygon points="0,400 0,523 90,523" fill="#6b6b6b"/>
    <polygon points="0,380 0,400 60,470" fill="#fff" opacity=".0"/>
  </svg>
  <div class="contact">
    <p>Raumfunke GmbH<br>Lindenkamp 14<br>22391 Hamburg</p>
    <p>+49 40 518 27 90<br>+49 171 402 83 61</p>
    <p>info@raumfunke.de</p>
  </div>
  <div class="url">www.raumfunke.de</div>
</section>

<!-- Innenseiten -->
<div class="spread-frame"></div>
<section class="page spread-left">
  <svg class="shapes" viewBox="0 0 370 523" aria-hidden="true">
    <path d="M0,60 Q190,20 370,30 L370,285 L0,300 Z" fill="#f5e44f"/>
    <polygon points="0,300 0,340 60,322" fill="#6b6b6b"/>
  </svg>
  <div class="tab" style="left:14px;top:64px">ÜBER UNS:</div>
  <div class="copy about">
    <p>Raumfunke ist eine junge Handelsvertretung im Norden Hamburgs. Durch das breite Produktsortiment unserer Hersteller gewährleisten wir Ihnen eine optimale Auswahl und Betreuung von der Planungsphase bis zur Installation.</p>
    <p>Auf Basis wirtschaftlicher, gestalterischer und technischer Bewertungskriterien beraten wir Sie bei der Auswahl Ihrer Beleuchtungsanlagen.</p>
    <p>Wir unterstützen Sie durch den Einsatz der richtigen Lichttechnik und tageslichtabhängigen Steuerungen dabei, Ihre Betriebskosten spürbar zu senken.</p>
    <p>Um für Sie die bestmöglichen Beleuchtungskonzepte realisieren zu können, ist für uns entsprechendes Know-how in Bezug auf gesetzliche Bestimmungen unerlässlich.</p>
    <p>Einen reibungslosen Projektverlauf garantieren wir durch einen dreistufigen Vertriebsweg und die Zusammenarbeit mit innovativen und flexiblen Partnern der Leuchtenindustrie.</p>
  </div>
  <div class="photo wood" style="left:30px;top:330px;width:160px;height:95px" role="img" aria-label="Foto: Empfangsbereich mit geschwungener Holzwand"></div>
  <div class="photo dark" style="left:196px;top:318px;width:160px;height:95px" role="img" aria-label="Foto: Großraumbüro mit Lichtbändern"></div>
  <div class="photo car" style="left:30px;top:432px;width:160px;height:80px" role="img" aria-label="Foto: Autohaus-Ausstellungsraum mit Deckenbeleuchtung"></div>
  <div class="photo office" style="left:196px;top:420px;width:160px;height:92px" role="img" aria-label="Foto: Empfangstresen mit linearen Deckenleuchten"></div>
  <svg class="shapes" viewBox="0 0 370 523" aria-hidden="true">
    <polygon points="190,492 190,512 168,512" fill="#f5e44f"/>
  </svg>
</section>

<section class="page spread-right">
  <div class="photo lamps" style="left:0;top:0;width:118px;height:120px" role="img" aria-label="Foto: runde Pendelleuchten vor grüner Wand"></div>
  <div class="photo office" style="left:122px;top:0;width:248px;height:72px" role="img" aria-label="Foto: Büroarbeitsplatz mit Fensterfront"></div>
  <div class="photo lobby" style="left:0;top:124px;width:192px;height:86px" role="img" aria-label="Foto: Lobby mit violetter Wandgestaltung"></div>
  <svg class="shapes" viewBox="0 0 370 523" aria-hidden="true">
    <polygon points="0,210 370,195 370,470 0,482" fill="#f5e44f"/>
    <polygon points="0,60 0,120 50,120" fill="#f5e44f"/>
    <polygon points="0,485 370,470 370,480 0,495" fill="#6b6b6b"/>
    <polygon points="0,497 370,482 370,500 0,515" fill="#f5e44f"/>
  </svg>
  <div class="range">
    <h3>UNSER LEISTUNGSSPEKTRUM<br>IM ÜBERBLICK:</h3>
    <ul>
      <li>Persönliche Beratung vor Ort</li>
      <li>Individuelle Lichtplanung</li>
      <li>Wirtschaftlichkeitsberechnung</li>
      <li>Sonderleuchtenentwicklung</li>
      <li>Produktschulungen</li>
      <li>Bemusterung der Leuchten</li>
      <li>Lieferung der Leuchten</li>
    </ul>
  </div>
  <div class="tab" style="left:12px;top:200px">SERVICE:</div>
  <div class="copy service-a">
    <p>In der heutigen Zeit ist angenehmes Licht immer wichtiger, die Anforderungen am Arbeitsplatz in öffentlichen und privaten Räumen an eine individuell ausgearbeitete Lichtplanung größer.</p>
    <p>Diese Probleme können mit verschiedensten Beleuchtungskonzepten und Lichtsystemen gelöst werden, welche sich durch Innovation und Bedienkomfort auszeichnen.</p>
    <p>Mit unserer Arbeitsplatzausleuchtung nach DIN-Norm, die Wirtschaftlichkeitsberechnung und persönliche Beratung vor Ort, haben wir eigene hohe Ansprüche an gelungenen Lichtlösungen.</p>
    <p>Durch die Zusammenarbeit mit unseren Leuchtenherstellern ist es uns möglich,</p>
  </div>
  <div class="copy service-b">
    <p>eigens für den Kunden Projektleuchten zu entwickeln und zu fertigen.</p>
    <p>In unserem neuen Showroom in Hamburg präsentieren wir auf 120 qm Ausstellungsfläche unseren interessierten Kunden eine große Auswahl an aktuellen Lichtsystemen von unseren renommierten Leuchtenherstellern.</p>
    <p>Lassen Sie sich hier von praktischen Beleuchtungsbeispielen und vielen Tipps zur kreativen Lichtplanung inspirieren.</p>
    <p>Unsere individuellen Lichtsysteme und Lichtsteuerungsanlagen geben Ihren Objekten eine neue Atmosphäre.</p>
    <p>Nutzen Sie die Möglichkeiten, durch Fachvorträge der Hersteller, Ihr Wissen rund um das Thema Beleuchtung zu erweitern.</p>
  </div>
</section>

</body>
</html>
```